Stationary Design Letterhead and Envelope

Artist should provide Letterhead and envelop stationary designs

Info for stationary:
Fernhallow Outdoor Advertising
4873 Quarry Rd. 915 N. PO BOX 528617
Austin, TX 78519

Dale Fernhallow
President
555-862-1907
dale@fernhallowsigns.example
fernhallowsigns.example

Target Market(s)

clients

Colors
0054AA
0677BA
7BADD7
CADEEF
E8F1F8

Requirements
Must have
• high quality unique eye catching and dynamic

```html
<!DOCTYPE html>
<html lang="en">
<head>
<meta charset="utf-8">
<title>Fernhallow Outdoor Advertising — Stationery</title>
<link href="https://fonts.googleapis.com/css2?family=Arimo:wght@400;700&family=Open+Sans:wght@700&family=Great+Vibes&display=swap" rel="stylesheet">
<style>
  :root {
    --brand-blue: #0a68a6;
    --brand-deep: #0054aa;
    --ink: #1d1d1d;
    --paper: #f3f3f3;
    --backdrop: #e4e4e4;
    --fold: #c9c9c9;
    --shadow: rgba(0,0,0,0.14);
  }
  * { box-sizing: border-box; margin: 0; padding: 0; }
  html, body { width: 1200px; height: 942px; overflow: hidden; }
  body {
    background: linear-gradient(180deg, #ededed 0%, var(--backdrop) 100%);
    font-family: "Arimo", Arial, sans-serif;
    color: var(--ink);
    position: relative;
  }
  .sheet {
    position: absolute;
    background: var(--paper);
    box-shadow: 0 2px 8px var(--shadow);
    overflow: hidden;
  }
  .brand-band { position: absolute; left: 0; right: 0; bottom: 0; height: 8px; background: var(--brand-blue); }

  .wordmark {
    font-family: "Open Sans", Arial, sans-serif;
    font-weight: 700;
    color: var(--brand-blue);
    line-height: 1;
    text-align: center;
  }
  .wordmark .name { display: block; font-size: 19px; letter-spacing: 0.5px; }
  .wordmark .tagline { display: block; font-size: 7.4px; letter-spacing: 0.2px; margin-top: 4px; }

  /* Letterhead */
  .letterhead { left: 157px; top: 150px; width: 437px; height: 618px; }
  .letterhead .wordmark { position: absolute; left: 0; right: 0; top: 35px; }
  .letter { position: absolute; left: 47px; top: 146px; width: 343px; font-size: 7.2px; line-height: 10.3px; }
  .letter p { margin-bottom: 10.3px; text-align: justify; }
  .letter .plain { text-align: left; }
  .letter .recipient { margin-top: 0; }
  .letter .salutation { margin-top: 20px; }
  .letter .closing { margin-top: 30px; margin-bottom: 0; }
  .signature { font-family: "Great Vibes", cursive; font-size: 15px; line-height: 20px; }

  .contact-block { font-size: 7.2px; line-height: 9px; }
  .contact-block .rule { width: 31px; height: 2px; background: var(--brand-blue); margin-bottom: 9px; }
  .contact-block .person { color: var(--brand-blue); font-weight: 700; font-size: 9px; }
  .contact-block .role { font-size: 7.2px; }
  .contact-block .role::before { content: "| "; color: var(--brand-blue); font-weight: 700; }
  .contact-line { display: flex; gap: 8px; }
  .contact-line span { display: inline-flex; align-items: center; gap: 2px; }
  .contact-line svg { width: 6px; height: 6px; fill: var(--brand-blue); }

  .letterhead .contact-block { position: absolute; left: 0; right: 0; top: 557px; text-align: center; }
  .letterhead .contact-block .rule { margin: 0 auto 9px; }
  .letterhead .contact-line { justify-content: center; }

  /* Envelope front */
  .envelope-front { left: 624px; top: 297px; width: 502px; height: 218px; }
  .envelope-front .wordmark { position: absolute; left: 32px; top: 30px; width: 124px; }
  .envelope-front .contact-block { position: absolute; left: 32px; top: 149px; }

  /* Envelope back */
  .envelope-back { left: 624px; top: 550px; width: 502px; height: 218px; }
  .envelope-back svg.flap { position: absolute; left: 0; top: 0; }
  .envelope-back .wordmark { position: absolute; left: 0; right: 0; top: 27px; color: #fff; }
  .envelope-back .web { position: absolute; left: 0; right: 0; top: 185px; text-align: center; font-size: 7.4px; letter-spacing: 1.1px; }
</style>
</head>
<body>

<section class="sheet letterhead">
  <div class="wordmark"><span class="name">FERNHALLOW</span><span class="tagline">OUTDOOR ADVERTISING</span></div>

  <div class="letter">
    <p class="plain">01 January 2050</p>
    <p class="plain recipient">Company (Pvt) Ltd.<br>PO Box 3355 Mainville St<br>Sample City Country 3355</p>
    <p class="plain salutation">Dear Peter Hollins,</p>
    <p>Lorem ipsum dolor sit amet, consectetuer adipiscing elit, sed diam nonummy nibh euismod tincidunt ut laoreet dolore magna aliquam erat volutpat. Ut wisi enim ad minim veniam, quis nostrud exerci tation ullamcorper suscipit lobortis nisl ut aliquip ex ea commodo consequat. Duis dolore te feugait nulla facilisi. Nam liber tempor cum soluta nobis eleifend option congue nihil imperdiet doming id quod mazim placerat facer possim assum. Lorem ipsum dolor sit amet, consectetuer adipiscing elit, sed diam nonummy nibh euismod tincidunt ut laoreet dolore magna aliquam erat volutpat. Ut wisi enim ad minim veniam, quis nostrud exerci tation ullamcorper suscipit lobortis nisl ut aliquip ex ea commodo consequat.</p>
    <p>Consectetuer adipiscing elit, sed diam nonummy nibh euismod tincidunt ut laoreet dolore magna aliquam erat volutpat. Ut wisi enim ad minim veniam, quis nostrud exerci tation ullamcorper suscipit lobortis nisl ut aliquip ex ea commodo consequat. Consectetuer adipiscing elit, sed diam nonummy nibh euismod tincidunt ut laoreet dolore magna aliquam erat volutpat. Ut wisi enim ad minim veniam, quis nostrud exerci tation ullamcorper suscipit lobortis nisl ut aliquip ex ea commodo consequat.</p>
    <p>Consectetuer adipiscing elit, sed diam nonummy nibh euismod tincidunt ut laoreet dolore magna aliquam erat volutpat. Ut wisi enim ad minim veniam, quis nostrud exerci tation ullamcorper suscipit lobortis nisl ut aliquip ex ea commodo consequat. Consectetuer adipiscing elit, sed diam nonummy nibh euismod tincidunt ut laoreet dolore magna aliquam erat volutpat. Ut wisi enim ad minim veniam, quis nostrud exerci tation ullamcorper suscipit lobortis nisl ut aliquip ex ea commodo consequat.</p>
    <p class="plain closing">Sincerely Yours</p>
    <p class="plain signature">William Ashgrove</p>
  </div>

  <div class="contact-block">
    <div class="rule"></div>
    <div><span class="person">Dale Fernhallow</span> <span class="role">President</span></div>
    <div>Fernhallow Outdoor Advertising, 4873 Quarry Rd. 915 N. PO BOX 528617, Austin, TX 78519</div>
    <div class="contact-line">
      <span><svg viewBox="0 0 10 10"><path d="M2 0.5l2 2-1 1.3c.6 1.3 1.6 2.3 2.9 2.9l1.3-1 2 2-1.3 1.8C4 9 1 6 0.5 1.8z"/></svg>555-862-1907</span>
      <span><svg viewBox="0 0 10 10"><path d="M0 2h10v6H0z"/><path d="M0 2l5 3.5L10 2" stroke="#f3f3f3" stroke-width=".8" fill="none"/></svg>dale@fernhallowsigns.example</span>
      <span><svg viewBox="0 0 10 10"><circle cx="5" cy="5" r="4.6"/><path d="M.5 5h9M5 .5c-2.4 2.6-2.4 6.4 0 9M5 .5c2.4 2.6 2.4 6.4 0 9" stroke="#f3f3f3" stroke-width=".7" fill="none"/></svg>www.fernhallowsigns.example</span>
    </div>
  </div>
  <div class="brand-band"></div>
</section>

<section class="sheet envelope-front">
  <div class="wordmark"><span class="name">FERNHALLOW</span><span class="tagline">OUTDOOR ADVERTISING</span></div>
  <div class="contact-block">
    <div class="rule"></div>
    <div><span class="person">Dale Fernhallow</span> <span class="role">President</span></div>
    <div>Fernhallow Outdoor Advertising, 4873 Quarry Rd. 915 N. PO BOX 528617, Austin, TX 78519</div>
    <div class="contact-line">
      <span><svg viewBox="0 0 10 10"><path d="M2 0.5l2 2-1 1.3c.6 1.3 1.6 2.3 2.9 2.9l1.3-1 2 2-1.3 1.8C4 9 1 6 0.5 1.8z"/></svg>555-862-1907</span>
      <span><svg viewBox="0 0 10 10"><path d="M0 2h10v6H0z"/><path d="M0 2l5 3.5L10 2" stroke="#f3f3f3" stroke-width=".8" fill="none"/></svg>dale@fernhallowsigns.example</span>
      <span><svg viewBox="0 0 10 10"><circle cx="5" cy="5" r="4.6"/><path d="M.5 5h9M5 .5c-2.4 2.6-2.4 6.4 0 9M5 .5c2.4 2.6 2.4 6.4 0 9" stroke="#f3f3f3" stroke-width=".7" fill="none"/></svg>www.fernhallowsigns.example</span>
    </div>
  </div>
  <div class="brand-band"></div>
</section>

<section class="sheet envelope-back">
  <svg class="flap" width="502" height="218" viewBox="0 0 502 218">
    <path d="M16 56 L6 210 Q6 216 12 218 M486 56 L496 210 Q496 216 490 218" fill="none" stroke="var(--fold)" stroke-width="0.8"/>
    <path d="M0 0 H502 L484 62 Q480 71 470 71 H32 Q22 71 18 62 Z" fill="var(--brand-blue)"/>
  </svg>
  <div class="wordmark"><span class="name">FERNHALLOW</span></div>
  <div class="web">www.fernhallowsigns.example</div>
</section>

</body>
</html>
```